BrambleWorks business card

Looking for business card design that supports our company/software values. We have 2 logo designs at the moment but open to change if you think you can enhance the brand. Check out website www.brambleworks.com.au.

Target Market(s)

Education

Contact Information for Business Card

Name, title, mobile, email and website

Font styles to use
Sans Serif

Colors

Designer to choose colors to be used in the design.

Requirements
Must have
• BrambleWorks logo with tree and tagline on rear side with dark grey background colour

```html
<!DOCTYPE html>
<html lang="en">
<head>
<meta charset="utf-8">
<title>BrambleWorks Business Card</title>
<link rel="stylesheet" href="https://fonts.googleapis.com/css2?family=Open+Sans:wght@400;600;700&display=swap">
<style>
  :root {
    --backdrop: #dcdcdc;
    --card-light: #f7f7f5;
    --card-dark: #1b1b1b;
    --ink-grey: #5f5f5f;
    --ink-soft: #6e6e6e;
    --leaf-green: #5e9e3a;
    --rule-grey: #8a8a8a;
    --emboss: #3b3b3b;
    --emboss-rule: #4a4a4a;
  }
  * { margin: 0; padding: 0; box-sizing: border-box; }
  html, body {
    width: 1200px; height: 856px; overflow: hidden;
    background: var(--backdrop);
    font-family: "Open Sans", sans-serif;
  }
  .canvas { position: relative; width: 1200px; height: 856px; }
  .card {
    position: absolute; width: 580px; height: 331px;
    box-shadow: 0 14px 30px rgba(0,0,0,0.18);
  }
  .card-front { left: 60px; top: 70px; background: var(--card-light); }
  .card-back { left: 560px; top: 455px; background: var(--card-dark); }

  .front-brand {
    position: absolute; left: 58px; top: 142px;
    display: flex; align-items: center; gap: 10px;
  }
  .brand-dot { width: 16px; height: 16px; border-radius: 50%; background: var(--leaf-green); }
  .brand-name {
    font-weight: 600; font-size: 26px; color: var(--ink-grey); letter-spacing: 0.2px;
  }
  .divider {
    position: absolute; left: 300px; top: 92px; width: 1px; height: 150px;
    background: var(--rule-grey);
  }
  .identity { position: absolute; left: 328px; top: 92px; }
  .person-name { font-weight: 700; font-size: 26px; color: var(--ink-grey); line-height: 1.1; }
  .person-title { font-weight: 400; font-size: 17px; color: var(--leaf-green); margin-top: 2px; }
  .contacts { position: absolute; left: 312px; top: 172px; list-style: none; }
  .contacts li {
    display: flex; align-items: center; gap: 12px;
    font-size: 16px; color: var(--ink-soft); height: 22px;
  }
  .contacts svg { width: 15px; height: 15px; fill: var(--leaf-green); flex: none; }

  .back-lockup { position: absolute; left: 130px; top: 110px; }
  .back-brand { display: flex; align-items: center; gap: 14px; }
  .back-brand .brand-dot { width: 22px; height: 22px; background: var(--emboss); }
  .back-brand .brand-name { font-size: 46px; color: var(--emboss); }
  .back-rule { width: 300px; height: 1px; background: var(--emboss-rule); margin: 6px 0 6px 36px; }
  .tagline { font-weight: 600; font-size: 17px; color: var(--emboss); margin-left: 36px; letter-spacing: 0.3px; }
</style>
</head>
<body>
<main class="canvas">
  <section class="card card-front">
    <div class="front-brand">
      <span class="brand-dot"></span>
      <span class="brand-name">BrambleWorks</span>
    </div>
    <div class="divider"></div>
    <div class="identity">
      <h1 class="person-name">Daniel Hart</h1>
      <p class="person-title">Director</p>
    </div>
    <ul class="contacts">
      <li>
        <svg viewBox="0 0 16 16"><path d="M4 1l2.5 3-1.5 2c.8 1.8 2.2 3.2 4 4l2-1.5 3 2.5-1.5 2.5C7 14.5 1.5 9 1.5 2.5z"/></svg>
        123.456.789.
      </li>
      <li>
        <svg viewBox="0 0 16 16"><path d="M4 1h8v14H4zM5.5 2.5v9.5h5V2.5zM8 12.8a.8.8 0 100 1.6.8.8 0 000-1.6z" fill-rule="evenodd"/></svg>
        123.456.789.
      </li>
      <li>
        <svg viewBox="0 0 16 16"><path d="M1 3h14v10H1zM1.5 3.5L8 9l6.5-5.5" stroke="#f7f7f5" stroke-width="1"/></svg>
        info@brambleworks.com.au
      </li>
      <li>
        <svg viewBox="0 0 16 16"><circle cx="8" cy="8" r="7"/><path d="M1 8h14M8 1c-3 3-3 11 0 14M8 1c3 3 3 11 0 14" stroke="#f7f7f5" stroke-width="1" fill="none"/></svg>
        www.brambleworks.com.au
      </li>
    </ul>
  </section>

  <section class="card card-back">
    <div class="back-lockup">
      <div class="back-brand">
        <span class="brand-dot"></span>
        <span class="brand-name">BrambleWorks</span>
      </div>
      <div class="back-rule"></div>
      <p class="tagline">Student Success Platform</p>
    </div>
  </section>
</main>
</body>
</html>
```